Menükarte für Weingastronomie
Zielgruppe
Wir betreiben einen eigenen Weinberg und stellen unseren eigenen Wein her - die Website ist gerade im Umbau https://oxal.hosting.trevanodienste.de/
Zielgruppe sind Weinliebhaber - für den Vertrieb bieten wir unseren Wein jetzt auch in der gehobenen Gastronomie.
Der Auftakt in der Gastronomie wird eine große Vertikal-Probe mit all unseren Jahrgängen, Menübegleitung und unserem Winzer sein.
Dafür soll es Tisch-Sets in DIN A3 geben.
Aufgabenstellung
BITTE DIE Platzierung der Gläser und der Teller beachten, so dass diese Platz haben. Zumindest die Weingläser mit deren 'Platzhalter' sollten in dem oberen Bereich angesiedelt sein. Sie Anlage/Datei.
Es soll eine historische Moselkarte als Grafik mit berücksichtigt werden - in Dateiupload enthalten.
Der Grundton des Sets soll grau sein, so ähnlich wie das Logo vom Restaurant (HALB - in Dateiupload enthalten)
OXAL Logo (unser Logo - ebenfalls in Dateiupload enthalten)

```html
<!DOCTYPE html>
<html lang="de">
<head>
<meta charset="utf-8">
<title>Vertikal Probe – OXAL Riesling 2011 - 2022</title>
<link href="https://fonts.googleapis.com/css2?family=Open+Sans:wght@400;600;700&family=Crimson+Text:wght@400;600&display=swap" rel="stylesheet">
<style>
  :root {
    --stage: #25272b;
    --paper: #efe7d6;
    --paper-edge: #e4dac4;
    --concrete-light: #b9b8b6;
    --concrete-dark: #a4a3a1;
    --disc: #4e4f51;
    --disc-ring: #eee5d3;
    --ink: #4b4c4e;
    --ink-soft: #6b6c6e;
    --tag: #c6dccd;
    --tag-deep: #9fbfab;
    --tag-ink: #5b7766;
    --map-paper: #eae1cb;
    --map-green: #c9d2b4;
    --map-frame: #8d8c86;
  }
  * { box-sizing: border-box; margin: 0; padding: 0; }
  html, body {
    width: 1200px; height: 3000px; overflow: hidden;
    background: var(--stage);
  }
  .placemat {
    position: absolute; left: 50px; top: 1112px;
    width: 1100px; height: 776px;
    background: var(--paper);
    box-shadow: 0 20px 60px rgba(0,0,0,.45);
  }
  .placemat-header {
    position: absolute; left: 0; top: 0; width: 100%; height: 116px;
    background: var(--paper);
    border-bottom: 2px solid var(--paper-edge);
  }
  .restaurant-name {
    position: absolute; left: 28px; top: 34px;
    font-family: "Open Sans", sans-serif; font-weight: 700;
    font-size: 40px; letter-spacing: 4px; color: var(--ink-soft);
    display: flex; align-items: center; gap: 12px;
  }
  .restaurant-name .mark {
    width: 22px; height: 22px; border-radius: 50%; background: var(--ink-soft);
  }
  .event-title {
    position: absolute; left: 280px; top: 32px;
    font-family: "Crimson Text", serif; font-size: 30px; color: var(--ink);
  }
  .event-subtitle {
    position: absolute; left: 497px; top: 42px;
    font-family: "Open Sans", sans-serif; font-size: 19px;
    letter-spacing: 4px; color: var(--ink-soft);
  }
  .winery-tag {
    position: absolute; left: 947px; top: 0; width: 129px; height: 190px;
    background: var(--tag);
    border: 4px solid var(--tag-deep);
    border-top: none;
    box-shadow: 0 6px 14px rgba(0,0,0,.2);
    z-index: 2;
    display: flex; flex-direction: column; align-items: center;
  }
  .winery-tag .winery-name {
    margin-top: 22px;
    font-family: "Crimson Text", serif; font-size: 46px; line-height: 1;
    color: var(--tag-ink);
  }
  .winery-tag .winery-mark {
    margin-top: 34px; width: 58px; height: 58px; background: var(--tag-deep);
  }
  .tasting-area {
    position: absolute; left: 0; top: 116px; width: 100%; height: 324px;
    background: radial-gradient(ellipse at 30% 40%, var(--concrete-light), var(--concrete-dark));
  }
  .glass-spot {
    position: absolute; width: 232px; height: 232px; top: 41px;
    border-radius: 50%; background: var(--disc);
    border: 9px solid var(--disc-ring);
    display: flex; align-items: center; justify-content: center;
  }
  .glass-spot::before {
    content: ""; position: absolute; inset: 9px;
    border-radius: 50%; border: 3px dotted #f2f2f2;
  }
  .glass-spot--first  { left: 162px; }
  .glass-spot--second { left: 433px; }
  .glass-spot--third  { left: 706px; }
  .vintage-list {
    text-align: center; color: #f4f4f4;
    font-family: "Open Sans", sans-serif; font-weight: 700; font-size: 15px; line-height: 21px;
  }
  .vintage-list .label { margin-bottom: 21px; }
  .map-area {
    position: absolute; left: 0; top: 440px; width: 100%; height: 336px;
    background: var(--paper);
  }
  .historic-map {
    position: absolute; left: 15px; top: 6px; width: 1072px; height: 324px;
    border: 4px double var(--map-frame);
    background:
      linear-gradient(175deg, transparent 40%, rgba(120,110,95,.25) 50%, transparent 60%),
      radial-gradient(ellipse at 30% 40%, var(--map-green), transparent 60%),
      radial-gradient(ellipse at 75% 60%, var(--map-green), transparent 55%),
      var(--map-paper);
  }
</style>
</head>
<body>
  <main class="placemat">
    <header class="placemat-header">
      <div class="restaurant-name"><span class="mark"></span>HALB</div>
      <h1 class="event-title">Vertikal Probe</h1>
      <p class="event-subtitle">OXAL RIESLING 2011 - 2022</p>
    </header>
    <div class="winery-tag">
      <span class="winery-name">OXAL</span>
      <span class="winery-mark"></span>
    </div>
    <section class="tasting-area">
      <div class="glass-spot glass-spot--first">
        <div class="vintage-list"><p class="label">OXAL</p><p>2022</p></div>
      </div>
      <div class="glass-spot glass-spot--second">
        <div class="vintage-list"><p class="label">OXAL</p><p>2021</p><p>2019</p><p>2017</p><p>2015</p><p>2013</p><p>2011</p></div>
      </div>
      <div class="glass-spot glass-spot--third">
        <div class="vintage-list"><p class="label">OXAL</p><p>2020</p><p>2018</p><p>2016</p><p>2014</p><p>2012</p><p>2011</p></div>
      </div>
    </section>
    <section class="map-area">
      <div class="historic-map" role="img" aria-label="Historische Weinbaukarte von Saar und Mosel mit dem Flusslauf und den Weinlagen"></div>
    </section>
  </main>
</body>
</html>
```